Refresh Existing Tradeshow Expo Booth

Scope: We're looking for a refresh of our existing tradeshow booth materials.

Business: IT Company specializing in Education service and support of mobile technology. We repair, service and support schools Zorvas, Velnotes, Plumeslates and other technology.

Core Message: No-sign-ups, diagnostic fees, troubleshooting, or complicated invoicing. Just pack and ship, and we handle the rest.

Tagline: We make 1:1 repairs easy, fast, and affordable.

Additional Resources: https://www.quillbranch.com/for-education/

Deliverables:
1 - 72" x 30" Banner Stand
1 - 8' Table Cloth Throw
1 - 2.5' x 8' Banner
Included in .psd or .ai files ready to print.

Materials Provided:
Brand Usage Guide
Sample Flyers / Marketing Materials
Original Vertical Banner Stand / Banner
Sample Messaging

Target Market(s)

IT Directors, Education, ED Tech

Industry/Entity Type

IT, Education

Other font styles liked:
• Dekar, Dekar Light

Colors
EB3D1F
EC4F4E
F09395
F8D3D4
FCEDEE

Requirements
Must have
• Clean Design, Not Busy, Crisp Lines, Brand Colors.

```html
<!DOCTYPE html>
<html lang="en">
<head>
<meta charset="utf-8">
<title>QuillBranch Tradeshow Booth Set</title>
<link rel="stylesheet" href="https://fonts.googleapis.com/css2?family=Roboto+Slab:wght@300;400;700&display=swap">
<style>
  :root {
    --brand-red: #e31e26;
    --brand-red-deep: #b3171d;
    --slate: #666666;
    --slate-text: #555555;
    --white: #ffffff;
  }
  * { margin: 0; padding: 0; box-sizing: border-box; }
  html, body { width: 754px; height: 1200px; overflow: hidden; }
  body {
    font-family: "Roboto Slab", Georgia, serif;
    background: linear-gradient(135deg, #d6d6d6 0%, #8e8e8e 45%, #555555 100%);
    position: relative;
  }
  .piece { position: absolute; overflow: hidden; }
  .piece svg.backdrop { position: absolute; left: 0; top: 0; }
  .abs { position: absolute; }
  .center { left: 0; width: 100%; text-align: center; }

  .brand-name { font-weight: 300; color: var(--slate-text); letter-spacing: 0.1em; white-space: nowrap; line-height: 1; }
  .brand-tag { font-weight: 300; color: var(--slate-text); letter-spacing: 0.14em; white-space: nowrap; line-height: 1; }
  .brand-dot { position: absolute; border-radius: 50%; background: var(--brand-red); }

  .tag-lead, .tag-tail { color: var(--slate-text); font-weight: 300; line-height: 1; white-space: nowrap; }
  .tag-main { color: var(--brand-red); font-weight: 700; line-height: 1; white-space: nowrap; letter-spacing: -0.01em; }
  .headline { color: var(--white); font-weight: 400; line-height: 1; white-space: nowrap; }
  .message { color: var(--white); font-weight: 300; }
  .phone { color: var(--white); font-weight: 700; line-height: 1; white-space: nowrap; }
  .contact { color: var(--white); font-weight: 400; line-height: 1; white-space: nowrap; }
  .contact i, .throw-contact i { display: inline-block; border-radius: 50%; background: var(--brand-red); vertical-align: middle; }

  .banner-stand { left: 263px; top: 70px; width: 230px; height: 552px; background: linear-gradient(180deg, #ffffff, #f1f1f1 25%); }
  .wide-banner { left: 176px; top: 664px; width: 404px; height: 126px; background: var(--white); }
  .table-throw { left: 176px; top: 836px; width: 404px; height: 276px; }
  .throw-field { position: absolute; inset: 0; background: linear-gradient(180deg, #f7f7f7, #ebebeb); }
  .throw-panel { position: absolute; left: 66px; top: 79px; width: 273px; height: 119px; background: var(--slate); }
  .throw-contact { color: var(--slate-text); line-height: 1; white-space: nowrap; }
</style>
</head>
<body>

<!-- Banner stand -->
<section class="piece banner-stand">
  <svg class="backdrop" width="230" height="552" viewBox="0 0 230 552">
    <defs>
      <linearGradient id="standPhoto" x1="0" y1="0" x2="0.4" y2="1">
        <stop offset="0" stop-color="#f1f1f1"/>
        <stop offset="0.12" stop-color="#ebe8e3"/>
        <stop offset="0.45" stop-color="#dcd2c6"/>
        <stop offset="0.75" stop-color="#c9ad95"/>
        <stop offset="1" stop-color="#b9a48f"/>
      </linearGradient>
      <radialGradient id="standPhotoAccent" cx="0.65" cy="0.7" r="0.45">
        <stop offset="0" stop-color="#d98a5a" stop-opacity="0.45"/>
        <stop offset="1" stop-color="#d98a5a" stop-opacity="0"/>
      </radialGradient>
      <radialGradient id="standDevices" cx="0.5" cy="0.5" r="0.5">
        <stop offset="0" stop-color="#ffffff"/>
        <stop offset="0.6" stop-color="#f2f2f2" stop-opacity="0.9"/>
        <stop offset="1" stop-color="#f2f2f2" stop-opacity="0"/>
      </radialGradient>
      <linearGradient id="standRed" x1="0" y1="0" x2="1" y2="0.3">
        <stop offset="0" stop-color="#e52228"/>
        <stop offset="1" stop-color="#cc121a"/>
      </linearGradient>
    </defs>
    <g role="img" aria-label="Photo of a teacher with a tablet and children working at a classroom table">
      <rect x="0" y="140" width="230" height="170" fill="url(#standPhoto)"/>
      <rect x="0" y="140" width="230" height="170" fill="url(#standPhotoAccent)"/>
    </g>
    <polygon points="0,302 230,252 230,456 0,505" fill="url(#standRed)"/>
    <polygon points="0,505 230,456 230,552 0,552" fill="var(--slate)"/>
    <ellipse cx="115" cy="302" rx="104" ry="56" fill="url(#standDevices)" role="img" aria-label="Laptop, desktop monitor, tablet and phone showing the brand screen"/>
  </svg>

  <span class="brand-dot" style="left:31px;top:26px;width:35px;height:35px"></span>
  <div class="abs brand-name" style="left:74px;top:31px;font-size:15px">QUILLBRANCH</div>
  <div class="abs brand-tag" style="left:74px;top:49px;font-size:7.5px">PHONE &amp; TABLET REPAIR</div>

  <div class="abs center tag-lead" style="top:78px;font-size:15px">WE MAKE</div>
  <div class="abs center tag-main" style="top:96px;font-size:20px">1:1 REPAIRS EASY,</div>
  <div class="abs center tag-tail" style="top:123px;font-size:15px">FAST, AND AFFORDABLE.</div>

  <div class="abs center headline" style="top:363px;font-size:29px">No-sign-ups</div>
  <p class="abs center message" style="top:402px;font-size:11.5px;line-height:15px;padding:0 24px">Diagnostic fees, troubleshooting, or complicated invoicing. Just pack and ship, and we handle the rest.</p>

  <div class="abs center phone" style="top:503px;font-size:22px">
    <svg width="11" height="11" viewBox="0 0 24 24" style="vertical-align:2px"><path fill="#fff" d="M6.6 10.8a15 15 0 0 0 6.6 6.6l2.2-2.2c.3-.3.7-.4 1-.2 1.1.4 2.3.6 3.6.6.6 0 1 .4 1 1V20c0 .6-.4 1-1 1A17 17 0 0 1 3 4c0-.6.4-1 1-1h3.5c.6 0 1 .4 1 1 0 1.3.2 2.5.6 3.6.1.3 0 .7-.2 1z"/></svg>
    555 014 2290
  </div>
  <div class="abs center contact" style="top:528px;font-size:6px">
    <i style="width:5px;height:5px"></i> www.quillbranch.com &nbsp;|&nbsp; <i style="width:5px;height:5px"></i> edu@quillbranch.com
  </div>
</section>

<!-- Horizontal banner -->
<section class="piece wide-banner">
  <svg class="backdrop" width="404" height="126" viewBox="0 0 404 126">
    <defs>
      <linearGradient id="widePhoto" x1="1" y1="0" x2="0.3" y2="1">
        <stop offset="0" stop-color="#eeebe7"/>
        <stop offset="0.4" stop-color="#ddd3c7"/>
        <stop offset="0.8" stop-color="#c9ad95"/>
        <stop offset="1" stop-color="#bb9c84"/>
      </linearGradient>
      <radialGradient id="widePhotoAccent" cx="0.3" cy="0.75" r="0.5">
        <stop offset="0" stop-color="#d98a5a" stop-opacity="0.45"/>
        <stop offset="1" stop-color="#d98a5a" stop-opacity="0"/>
      </radialGradient>
      <radialGradient id="wideDevices" cx="0.5" cy="0.5" r="0.5">
        <stop offset="0" stop-color="#ffffff"/>
        <stop offset="0.6" stop-color="#f2f2f2" stop-opacity="0.85"/>
        <stop offset="1" stop-color="#f2f2f2" stop-opacity="0"/>
      </radialGradient>
    </defs>
    <polygon points="149,0 289,0 256,126 116,126" fill="var(--brand-red)"/>
    <polygon points="215,0 289,0 266,88" fill="var(--brand-red-deep)"/>
    <g role="img" aria-label="Photo of children and a teacher with tablets at a classroom table">
      <polygon points="289,0 404,0 404,126 256,126" fill="url(#widePhoto)"/>
      <polygon points="289,0 404,0 404,126 256,126" fill="url(#widePhotoAccent)"/>
    </g>
    <polygon points="0,95 124,95 116,126 0,126" fill="var(--slate)"/>
    <ellipse cx="206" cy="44" rx="64" ry="36" fill="url(#wideDevices)" role="img" aria-label="Laptop, desktop monitor, tablet and phone showing the brand screen"/>
  </svg>

  <span class="brand-dot" style="left:14px;top:14px;width:23px;height:23px"></span>
  <div class="abs brand-name" style="left:41px;top:17px;font-size:9.5px">QUILLBRANCH</div>
  <div class="abs brand-tag" style="left:41px;top:29px;font-size:4.8px">PHONE &amp; TABLET REPAIR</div>

  <div class="abs tag-lead" style="left:0;width:130px;text-align:center;top:46px;font-size:8.5px">WE MAKE</div>
  <div class="abs tag-main" style="left:0;width:130px;text-align:center;top:57px;font-size:11.5px">1:1 REPAIRS EASY,</div>
  <div class="abs tag-tail" style="left:0;width:130px;text-align:center;top:73px;font-size:8.5px">FAST, AND AFFORDABLE.</div>

  <div class="abs phone" style="left:6px;width:112px;text-align:center;top:100px;font-size:14px">555 014 2290</div>
  <div class="abs contact" style="left:6px;width:112px;text-align:center;top:117px;font-size:4px">
    <i style="width:3px;height:3px"></i> www.quillbranch.com | <i style="width:3px;height:3px"></i> edu@quillbranch.com
  </div>

  <div class="abs headline" style="left:134px;width:120px;text-align:center;top:82px;font-size:15px">No-sign-ups</div>
  <p class="abs message" style="left:138px;width:112px;text-align:center;top:100px;font-size:5px;line-height:6.5px">Diagnostic fees, troubleshooting, or complicated Invoicing. Just pack and ship, and we handle the rest.</p>
</section>

<!-- Table throw -->
<section class="piece table-throw">
  <div class="throw-field" role="img" aria-label="Faint repeating brand pattern on a light grey cloth"></div>
  <div class="throw-panel"></div>

  <span class="brand-dot" style="left:130px;top:122px;width:33px;height:33px"></span>
  <div class="abs brand-name" style="left:169px;top:126px;font-size:14px;color:#fff">QUILLBRANCH</div>
  <div class="abs brand-tag" style="left:169px;top:143px;font-size:7px;color:#fff">PHONE &amp; TABLET REPAIR</div>

  <div class="abs tag-lead" style="left:48px;width:120px;text-align:center;top:220px;font-size:7px">WE MAKE</div>
  <div class="abs tag-main" style="left:48px;width:120px;text-align:center;top:229px;font-size:9.5px">1:1 REPAIRS EASY,</div>
  <div class="abs tag-tail" style="left:48px;width:120px;text-align:center;top:241px;font-size:7px">FAST, AND AFFORDABLE.</div>

  <span class="brand-dot" style="left:167px;top:224px;width:18px;height:18px"></span>
  <div class="abs brand-name" style="left:190px;top:227px;font-size:8.5px">QUILLBRANCH</div>
  <div class="abs brand-tag" style="left:190px;top:238px;font-size:4.2px">PHONE &amp; TABLET REPAIR</div>

  <div class="abs throw-contact" style="left:268px;top:221px;font-size:10.5px;font-weight:700">555 014 2290</div>
  <div class="abs throw-contact" style="left:268px;top:234px;font-size:5.5px"><i style="width:5px;height:5px"></i> www.quillbranch.com</div>
  <div class="abs throw-contact" style="left:268px;top:243px;font-size:5.5px"><i style="width:5px;height:5px"></i> edu@quillbranch.com</div>
</section>

</body>
</html>
```